Business card for Chiropractic clinics needs reworked / redesigned

The business card in attachment was designed 10 years ago. It is in need of an update.
We have 2 clinics:
VELDHOVE KLINIEK & VELDHOVE KLINIEK NOORD
Only one address needs to be on the card for doctors that only work in one clinic and two addresses need to be on the card for the doctors that work in both clinics.

Target Market(s)

patients/referrers

Industry/Entity Type

Medical

Contact Information for Business Card

Logo (in full or zoomed-in)
Clinic Name
Doctor name and title
clinic address, website, tel, email

Font styles to use
Sans Serif

Colors

Designer to choose colors to be used in the design.

Requirements
Must have
• Good contrast/readability
• We like modern minimalistic designs
• The Bcard needs to project our very high standard of proficiency/professionalism
Should not have
• Not curly
• Not to much colours

```html
<!DOCTYPE html>
<html lang="en">
<head>
<meta charset="utf-8">
<title>Veldhove Kliniek – Business Card</title>
<link href="https://fonts.googleapis.com/css2?family=Barlow+Condensed:wght@600&family=Open+Sans:wght@400;600&family=Poppins:wght@400&display=swap" rel="stylesheet">
<style>
  :root {
    --navy: #1d4a7a;
    --sky: #29a3dd;
    --ink: #3d3d3d;
    --paper: #ffffff;
    --stage: #eef0f2;
  }
  * { margin: 0; padding: 0; box-sizing: border-box; }
  html, body { width: 1200px; height: 830px; overflow: hidden; }
  body { background: var(--stage); position: relative; font-family: "Open Sans", sans-serif; }

  .card {
    position: absolute; left: 100px; top: 137px;
    width: 1000px; height: 556px;
    background: var(--paper);
    box-shadow: 0 6px 24px rgba(0,0,0,.12);
    overflow: hidden;
  }
  .side-band {
    position: absolute; right: 0; top: 0;
    width: 72px; height: 100%;
    background: var(--sky);
  }
  .side-band svg { position: absolute; left: 0; top: 209px; }

  .brand { position: absolute; left: 74px; top: 86px; display: flex; align-items: center; gap: 18px; }
  .brand-dot { width: 26px; height: 26px; border-radius: 50%; background: var(--sky); }
  .brand-name {
    font-family: "Barlow Condensed", sans-serif; font-weight: 600;
    font-size: 56px; line-height: 1; color: var(--navy); letter-spacing: 1px;
  }
  .clinic-address {
    position: absolute; left: 118px; top: 150px;
    font-size: 27px; line-height: 33px; color: var(--sky);
  }

  .doctor { position: absolute; right: 90px; top: 212px; text-align: right; }
  .doctor-name {
    font-family: "Poppins", sans-serif; font-size: 40px; line-height: 1.1;
    color: var(--navy); letter-spacing: -.5px;
  }
  .doctor-title {
    margin-top: 10px; font-size: 25px; font-weight: 600;
    letter-spacing: 4px; color: var(--navy); padding-right: 8px;
  }

  .contacts { position: absolute; left: 40px; top: 378px; list-style: none; }
  .contacts li {
    display: flex; align-items: center; gap: 20px;
    font-size: 27px; line-height: 36px; color: var(--ink);
  }
  .contacts svg { width: 22px; height: 22px; flex: none; }

  .license-number {
    position: absolute; right: 86px; top: 466px;
    font-size: 24px; color: var(--ink);
  }
  .base-rule {
    position: absolute; left: 0; top: 509px;
    width: 928px; height: 6px; background: var(--navy);
  }
</style>
</head>
<body>
  <article class="card">
    <div class="side-band">
      <svg width="46" height="54" viewBox="0 0 46 54"><polygon points="0,0 46,27 0,54" fill="var(--paper)"/></svg>
    </div>

    <div class="brand">
      <span class="brand-dot"></span>
      <h1 class="brand-name">VELDHOVE KLINIEK</h1>
    </div>
    <p class="clinic-address">Lindelaan 48<br>9000 Veldhove</p>

    <div class="doctor">
      <p class="doctor-name">Pieter VANLAERE D.C.</p>
      <p class="doctor-title">CHIROPRACTOR</p>
    </div>

    <ul class="contacts">
      <li>
        <svg viewBox="0 0 24 24"><path fill="var(--sky)" d="M6.6 10.8a15.1 15.1 0 0 0 6.6 6.6l2.2-2.2a1 1 0 0 1 1-.25 11.4 11.4 0 0 0 3.6.57 1 1 0 0 1 1 1V20a1 1 0 0 1-1 1A17 17 0 0 1 3 4a1 1 0 0 1 1-1h3.5a1 1 0 0 1 1 1c0 1.25.2 2.45.57 3.57a1 1 0 0 1-.25 1z"/></svg>
        32(0)9 310 45 82
      </li>
      <li>
        <svg viewBox="0 0 24 24"><rect x="2" y="5" width="20" height="14" rx="1" fill="var(--sky)"/><path d="M3 6l9 7 9-7" fill="none" stroke="var(--paper)" stroke-width="1.6"/></svg>
        info@veldhovekliniek.be
      </li>
      <li>
        <svg viewBox="0 0 24 24"><circle cx="12" cy="12" r="10" fill="var(--sky)"/><path d="M2 12h20M12 2c3 3 3 17 0 20M12 2c-3 3-3 17 0 20" fill="none" stroke="var(--paper)" stroke-width="1.4"/></svg>
        www.veldhovekliniek.be
      </li>
    </ul>

    <p class="license-number">0.47265/81.000</p>
    <div class="base-rule"></div>
  </article>
</body>
</html>
```